Illustrationen für Unternehmensberatung im Bereich der Vorsorge- und Notfallplanung
ich bin hoch zufrieden mit dem Ergebnis. Vor allem ging alles ganz schnell und unkompliziert. Danke auch an dieser Stelle an Lennart :-)
Zielgruppe
wir beraten kleine und mittelständige Unternehmer/Innen im Bereich der Vorsorge- und Notfallplanung, sowohl im privaten wie im betrieblichen Bereich.
Aufgabenstellung
Die Illustrationen sollten das Niveau von freiberuflich, selbständig Tätigen und von Unternehmern treffen. Nicht zu verspielt, seriös und für eine Zielgruppe ab 35 Jahren geeignet.

```html
<!DOCTYPE html>
<html lang="de">
<head>
<meta charset="utf-8">
<title>Unternehmer-Beratung ganzheitlich definiert</title>
<link rel="stylesheet" href="https://fonts.googleapis.com/css2?family=Open+Sans:wght@400;600;700&display=swap">
<style>
  :root {
    --ink: #ffffff;
    --ink-soft: rgba(255,255,255,0.85);
    --bg-deep: #0b2a45;
    --bg-mid: #14507a;
    --bg-light: #2a7cab;
    --bubble-fill: #ffffff;
    --bubble-ink: #0f3a5c;
  }
  html, body {
    margin: 0;
    padding: 0;
    width: 1200px;
    height: 849px;
    overflow: hidden;
    background: var(--bg-deep);
  }
  .canvas {
    position: relative;
    width: 1200px;
    height: 849px;
    overflow: hidden;
    font-family: "Open Sans", Arial, sans-serif;
    color: var(--ink);
  }
  .backdrop {
    position: absolute;
    inset: 0;
    background:
      radial-gradient(ellipse 380px 420px at 90px 430px, rgba(60,130,175,0.55), transparent 70%),
      radial-gradient(ellipse 300px 360px at 620px 360px, rgba(20,60,95,0.7), transparent 70%),
      radial-gradient(ellipse 320px 380px at 1080px 380px, rgba(70,150,195,0.5), transparent 70%),
      linear-gradient(180deg, var(--bg-light) 0%, var(--bg-mid) 45%, var(--bg-deep) 100%);
  }
  .backdrop::after {
    content: "";
    position: absolute;
    inset: 0;
    background: rgba(8,40,70,0.35);
  }
  .diagram {
    position: absolute;
    inset: 0;
  }
  .headline {
    position: absolute;
    top: 28px;
    left: 0;
    width: 100%;
    text-align: center;
    font-size: 28px;
    font-weight: 400;
    margin: 0;
  }
  .headline strong { font-weight: 700; }
  .core {
    position: absolute;
    top: 368px;
    left: 0;
    width: 100%;
    text-align: center;
    font-size: 27px;
    font-weight: 700;
    line-height: 35px;
    margin: 0;
  }
  .role {
    position: absolute;
    transform: translateX(-50%);
    white-space: nowrap;
    font-size: 15px;
    font-weight: 700;
    text-align: center;
    line-height: 23px;
  }
  .role .thin { font-weight: 400; }
  .level {
    position: absolute;
    text-align: center;
    font-size: 19px;
    font-weight: 700;
    line-height: 25px;
  }
  .closing {
    position: absolute;
    top: 776px;
    left: 0;
    width: 100%;
    text-align: center;
    font-size: 34px;
    font-weight: 700;
    margin: 0;
  }
</style>
</head>
<body>
<div class="canvas">
  <div class="backdrop" role="img" aria-label="Unscharfes Foto einer Besprechung von Geschäftsleuten in Blautönen"></div>

  <svg class="diagram" width="1200" height="849" viewBox="0 0 1200 849" aria-hidden="true">
    <defs>
      <symbol id="docs" viewBox="0 0 34 30">
        <g fill="none" stroke="#fff" stroke-width="1.6" stroke-linejoin="round">
          <path d="M2 2h14l4 4v12H2z"/>
          <path d="M8 7h14l4 4v12H8z" fill="rgba(20,70,105,0.6)"/>
          <path d="M14 12h14l4 4v12H14z" fill="rgba(20,70,105,0.6)"/>
          <path d="M28 12v4h4"/>
        </g>
      </symbol>
    </defs>

    <g class="axis" stroke="#fff" stroke-width="1.4" opacity="0.8">
      <line x1="0" y1="409" x2="320" y2="409"/>
      <line x1="872" y1="409" x2="1200" y2="409"/>
    </g>

    <g class="connectors" stroke="#fff" stroke-width="1.4" stroke-dasharray="2 4" fill="none">
      <line x1="299" y1="239" x2="470" y2="356"/>
      <line x1="463" y1="164" x2="549" y2="349"/>
      <line x1="616" y1="142" x2="616" y2="214"/>
      <line x1="798" y1="171" x2="713" y2="353"/>
      <line x1="969" y1="235" x2="834" y2="353"/>
      <line x1="256" y1="339" x2="313" y2="368"/>
      <line x1="969" y1="363" x2="891" y2="378"/>
      <line x1="228" y1="484" x2="306" y2="459"/>
      <line x1="228" y1="584" x2="356" y2="470"/>
      <line x1="278" y1="638" x2="456" y2="477"/>
      <line x1="442" y1="672" x2="527" y2="484"/>
      <line x1="627" y1="650" x2="627" y2="587"/>
      <line x1="791" y1="655" x2="713" y2="484"/>
      <line x1="983" y1="648" x2="791" y2="470"/>
      <line x1="998" y1="534" x2="855" y2="463"/>
      <line x1="998" y1="463" x2="876" y2="442"/>
    </g>

    <g class="bubbles" fill="none" stroke="#fff" stroke-width="2">
      <path d="M553 235h162v58h-40l-10 14-4-14H553z"/>
      <path d="M553 509h159v60h-43l-10 14-4-14H553z"/>
    </g>

    <g class="icons">
      <use href="#docs" x="418" y="112" width="34" height="30"/>
      <use href="#docs" x="599" y="91" width="34" height="30"/>
      <use href="#docs" x="774" y="112" width="34" height="30"/>
      <use href="#docs" x="225" y="155" width="34" height="30"/>
      <use href="#docs" x="963" y="169" width="34" height="30"/>
      <use href="#docs" x="151" y="266" width="34" height="30"/>
      <use href="#docs" x="1009" y="295" width="34" height="30"/>
      <use href="#docs" x="128" y="459" width="34" height="30"/>
      <use href="#docs" x="1037" y="437" width="34" height="30"/>
      <use href="#docs" x="100" y="571" width="34" height="30"/>
      <use href="#docs" x="1037" y="533" width="34" height="30"/>
      <use href="#docs" x="154" y="661" width="34" height="30"/>
      <use href="#docs" x="1009" y="639" width="34" height="30"/>
      <use href="#docs" x="396" y="675" width="34" height="30"/>
      <use href="#docs" x="610" y="654" width="34" height="30"/>
      <use href="#docs" x="788" y="661" width="34" height="30"/>
    </g>
  </svg>

  <h1 class="headline">Unternehmer-Beratung <strong>ganzheitlich</strong> definiert</h1>

  <div class="level" style="left:553px; top:239px; width:162px;">persönliche /<br>private Ebene</div>
  <div class="level" style="left:553px; top:514px; width:159px;">geschäftliche<br>Ebene</div>

  <p class="core">Unternehmen / in - Persönlichkeiten<br>in unterschiedlichen Rollen</p>

  <div class="role" style="left:435px; top:139px;">Versorger</div>
  <div class="role" style="left:616px; top:117px;">Mensch</div>
  <div class="role" style="left:791px; top:142px;">Mutter / Vater</div>
  <div class="role" style="left:245px; top:178px;">Tochter / Sohn</div>
  <div class="role" style="left:980px; top:195px;">Ehefrau / -mann</div>
  <div class="role" style="left:150px; top:294px;">Schwester / Bruder</div>
  <div class="role" style="left:1036px; top:319px;">Freundin / Freund</div>
  <div class="role" style="left:147px; top:481px;">Ausbilder</div>
  <div class="role" style="left:1054px; top:461px;">Gesellschafter</div>
  <div class="role" style="left:120px; top:596px;">Vorgesetzter</div>
  <div class="role" style="left:1054px; top:557px;">Kaufmann</div>
  <div class="role" style="left:175px; top:686px;">Entscheider</div>
  <div class="role" style="left:1026px; top:663px;">Verkäufer</div>
  <div class="role" style="left:415px; top:698px;">Entscheider</div>
  <div class="role" style="left:627px; top:682px;">Unternehmer <span class="thin">ist</span><br><span class="thin">das Gegenteil von</span><br>Unterlasser</div>
  <div class="role" style="left:805px; top:689px;">Visionär</div>

  <p class="closing">Viele Rollen für einen Menschen, oder ?</p>
</div>
</body>
</html>
```